KORVELLA Corporate Business Card

Modern business card design for company which focuses in the areas of Staffing, IT Consulting & Data Services. Please note: We are no longer using the IT subscript on the logo. All designs should have IT subscript removed.
Website: www.korvellait.example

```html
<!DOCTYPE html>
<html lang="en">
<head>
<meta charset="utf-8">
<title>KORVELLA Corporate Business Card</title>
<link href="https://fonts.googleapis.com/css2?family=Lato:wght@400;700&display=swap" rel="stylesheet">
<style>
  :root{
    --bg:#3a3a3d;
    --blue-deep:#15599a;
    --blue-bright:#2a9ad8;
    --blue-mid:#1f7fc4;
    --card-dark:#1d1c22;
    --ink-light:#ffffff;
    --ink-soft:#c9cbd2;
    --rule:#5a5a62;
  }
  *{margin:0;padding:0;box-sizing:border-box}
  html,body{width:1200px;height:1015px;overflow:hidden}
  body{background:var(--bg);font-family:"Lato",Arial,sans-serif;position:relative}

  .card{position:absolute;left:250px;width:700px;height:400px;overflow:hidden;box-shadow:0 14px 30px rgba(0,0,0,.45)}
  .card-front{top:85px;background:linear-gradient(180deg,var(--blue-deep) 0%,var(--blue-bright) 100%);color:var(--ink-light);text-align:center}
  .card-back{top:530px;background:var(--card-dark)}

  .brand{display:flex;align-items:center;gap:14px;font-weight:700;letter-spacing:4px;line-height:1}
  .brand-mark{width:38px;height:38px;border-radius:4px}
  .card-front .brand{position:absolute;top:110px;left:0;right:0;justify-content:center;font-size:60px;color:var(--ink-light)}
  .card-front .brand-mark{background:var(--ink-light)}

  .front-rule{position:absolute;top:210px;left:190px;right:190px;height:1px;background:rgba(255,255,255,.35)}
  .services{position:absolute;top:232px;left:0;right:0;list-style:none;font-size:19px;line-height:27px;color:var(--ink-light)}

  .card-back .brand{position:absolute;top:175px;left:60px;font-size:50px;color:var(--blue-bright)}
  .card-back .brand-mark{width:32px;height:32px;background:var(--blue-bright)}

  .back-divider{position:absolute;top:40px;left:400px;width:1px;height:225px;background:var(--rule)}
  .contact{position:absolute;top:50px;left:425px;color:var(--ink-soft);font-size:18px}
  .contact-name{color:var(--blue-bright);font-size:22px;font-weight:400;letter-spacing:.5px}
  .contact-title{font-size:18px;margin-bottom:10px}
  .contact-list{list-style:none}
  .contact-list li{display:flex;align-items:center;gap:9px;line-height:26px}
  .contact-list svg{width:14px;height:14px;flex:none;fill:var(--blue-bright)}
  .contact-address{margin-top:14px;line-height:24px}

  .band-light{position:absolute;left:0;bottom:0;width:385px;height:20px;background:var(--blue-bright)}
  .band-deep{position:absolute;right:0;bottom:0;width:315px;height:42px;background:var(--blue-mid);border-left:4px solid var(--card-dark)}
</style>
</head>
<body>

<section class="card card-front" aria-label="Business card front">
  <div class="brand"><span class="brand-mark"></span><span class="brand-name">KORVELLA</span></div>
  <div class="front-rule"></div>
  <ul class="services">
    <li>Staff Augmentation &amp; Recruiting</li>
    <li>Database Administration Services (DBA)</li>
    <li>Project Management &amp;Application Development</li>
    <li>Business Intelligence &amp; Analytics | Internet of Things (IoT)</li>
  </ul>
</section>

<section class="card card-back" aria-label="Business card back">
  <div class="brand"><span class="brand-mark"></span><span class="brand-name">KORVELLA</span></div>
  <div class="back-divider"></div>
  <div class="contact">
    <h1 class="contact-name">MARCUS DELANE</h1>
    <p class="contact-title">Managing Director</p>
    <ul class="contact-list">
      <li><svg viewBox="0 0 16 16" aria-hidden="true"><path d="M3 1h3l1.5 4-2 1.3a9 9 0 0 0 4.2 4.2L11 8.5l4 1.5v3a2 2 0 0 1-2 2A12 12 0 0 1 1 3a2 2 0 0 1 2-2z"/></svg>555-014-2290</li>
      <li><svg viewBox="0 0 16 16" aria-hidden="true"><path d="M1 3h14v10H1z M2 4.2v.4l6 4.2 6-4.2v-.4z" fill-rule="evenodd"/></svg>contactus@korvellait.example</li>
      <li><svg viewBox="0 0 16 16" aria-hidden="true"><path d="M8 1a7 7 0 1 0 0 14A7 7 0 0 0 8 1zm0 2.2L12 8l-4 4.8L4 8z" fill-rule="evenodd"/></svg>www.korvellait.example</li>
    </ul>
    <p class="contact-address">418 Alder Lane<br>Brookhaven, OH 45010</p>
  </div>
  <div class="band-light"></div>
  <div class="band-deep"></div>
</section>

</body>
</html>
```